We need a laundry sheet packingbox desgin

-look at our website kribbelnest.nl to be in line with our house style/collor
We are a perfume seller and would like to offer also wasshingsheets with NO SMELL, so the customers can buy this incombination with our washingperfumes.
-the wassingheets will be neutrale(NO SMELL)
-it will be for the Dutch market
The next points should be on the desgin of the package
-our brand name: KRIBBELNEST
-product name: WASSTRIPS
-(contains) Bevat: 30 wasstrips
-30 wasstrips = 60 wasbeurten
Please take some inspiration of others sellers & regarding eco friendly symbols etc.:
velondra.com & plumtak.nl
Backside information will be provided afther we found the right desgin
Please look at attachement pdf open box.
Here you can find the pdf design where you need to customize:
https://qx.vz/t-rKbWnHs4Lp

```html
<!DOCTYPE html>
<html lang="nl">
<head>
<meta charset="utf-8">
<title>Kribbelnest Wasstrips – verpakking voorkant en zijkant</title>
<link href="https://fonts.googleapis.com/css2?family=Playfair+Display:wght@600;800&family=Poppins:wght@400;600&display=swap" rel="stylesheet">
<style>
  :root {
    --stage: #3a3a3a;
    --paper: #f3f2f0;
    --gold-deep: #b97f2c;
    --gold-mid: #c99a3c;
    --gold-light: #dcb652;
    --spine-gold: #d9ad48;
    --brand-gold: #b8862f;
    --ink: #111111;
    --white: #ffffff;
  }
  * { box-sizing: border-box; margin: 0; padding: 0; }
  html, body {
    width: 900px; height: 1200px; overflow: hidden;
    background: var(--stage);
  }
  .package {
    position: absolute; left: 95px; top: 50px;
    width: 710px; height: 1100px;
    display: flex;
  }
  .box-spine {
    position: relative;
    width: 70px; height: 1100px;
    background: linear-gradient(180deg, var(--spine-gold) 0%, var(--gold-mid) 50%, var(--spine-gold) 100%);
    display: flex; align-items: center; justify-content: center;
  }
  .spine-name {
    writing-mode: vertical-rl;
    font-family: "Playfair Display", serif; font-weight: 600;
    font-size: 30px; letter-spacing: 2px; color: var(--white);
    line-height: 1;
  }
  .box-front {
    position: relative;
    width: 640px; height: 1100px;
    background: linear-gradient(160deg, var(--gold-deep) 0%, var(--gold-mid) 50%, var(--gold-light) 100%);
    overflow: hidden;
  }
  .wave-top { position: absolute; inset: 0; width: 640px; height: 1100px; }
  .brand {
    position: absolute; top: 110px; left: 0; width: 640px;
    display: flex; flex-direction: column; align-items: center; gap: 18px;
  }
  .brand-dot {
    width: 70px; height: 70px; border-radius: 50%;
    background: var(--brand-gold);
  }
  .brand-name {
    font-family: "Playfair Display", serif; font-weight: 600;
    font-size: 26px; letter-spacing: 1px; color: var(--brand-gold);
  }
  .product-name {
    position: absolute; left: 50px; top: 520px;
    font-family: "Playfair Display", serif; font-weight: 800;
    font-size: 88px; letter-spacing: -1px; color: var(--white);
    line-height: 1;
  }
  .claims {
    position: absolute; left: 54px; top: 652px;
    font-family: "Poppins", sans-serif; font-size: 21px; line-height: 29px;
    color: var(--white);
  }
  .claims strong { font-weight: 600; }
  .usage-steps {
    position: absolute; left: 54px; top: 770px;
    width: 540px; height: 150px; border-radius: 6px;
    background: linear-gradient(90deg, rgba(255,255,255,0.14), rgba(255,255,255,0.08));
  }
  .contents {
    position: absolute; left: 0; width: 640px; top: 975px;
    display: flex; gap: 70px; align-items: center; justify-content: center;
    font-family: "Poppins", sans-serif; color: var(--white);
  }
  .contents-item { display: flex; align-items: center; gap: 12px; }
  .contents-value { font-size: 28px; font-weight: 600; line-height: 1; }
  .contents-label { font-size: 14px; line-height: 1.3; }
</style>
</head>
<body>
  <div class="package">
    <aside class="box-spine">
      <span class="spine-name">KRIBBELNEST</span>
    </aside>

    <main class="box-front">
      <svg class="wave-top" viewBox="0 0 640 1100" aria-hidden="true">
        <path d="M0 0 H640 V648 C582 470 456 360 287 312 C155 272 58 170 0 10 Z" fill="var(--paper)"/>
        <path d="M0 10 C58 170 155 272 287 312 C456 360 582 470 640 648" fill="none" stroke="var(--ink)" stroke-width="8"/>
      </svg>

      <header class="brand">
        <span class="brand-dot"></span>
        <span class="brand-name">KRIBBELNEST</span>
      </header>

      <h1 class="product-name">WASSTRIPS</h1>

      <p class="claims">
        <strong>60 wasbeurten</strong> per verpakking<br>
        100% <strong>Milieuvriendelijk</strong><br>
        Geschikt voor alle wasbehoeften
      </p>

      <div class="usage-steps" role="img" aria-label="Gebruiksillustratie: vuil shirt plus wasstrip, in de wasmachine, schoon shirt"></div>

      <section class="contents">
        <div class="contents-item">
          <svg width="76" height="64" viewBox="0 0 76 64" aria-hidden="true">
            <path d="M22 2 H74 L54 58 H2 Z" fill="var(--white)"/>
          </svg>
          <div><div class="contents-value">30</div><div class="contents-label">wasstrips</div></div>
        </div>
        <div class="contents-item">
          <svg width="60" height="64" viewBox="0 0 60 64" aria-hidden="true">
            <rect x="3" y="3" width="54" height="58" rx="5" fill="none" stroke="var(--white)" stroke-width="3"/>
            <circle cx="30" cy="34" r="16" fill="none" stroke="var(--white)" stroke-width="3"/>
          </svg>
          <div><div class="contents-value">60</div><div class="contents-label">wasbeurten</div></div>
        </div>
      </section>
    </main>
  </div>
</body>
</html>
```